Consulting company needs Business Cards - rough concept provided

I'm looking for someone to take our business card idea and make is slick and polished - to communicate our high-end, sophisticated, serious consulting business. We have a rough layout we did in-house. We are open to ideas on repo-ing elements, adjusting sizes, typefaces etc... within the general concept we've already come up with. We want it to be super-clean and sophisticated. We want to keep the white backgrounds, and blue brand colors. Our goal is to print with painted blue edges on thick cardstock. Thank you!!

```html
<!DOCTYPE html>
<html lang="en">
<head>
<meta charset="utf-8">
<title>Brightfable Business Cards</title>
<link href="https://fonts.googleapis.com/css2?family=Montserrat:wght@400;700;800&display=swap" rel="stylesheet">
<style>
  :root {
    --brand-blue: #0a8fd6;
    --ink: #1c1c1c;
    --muted: #b4b4b4;
    --rule: #7a7a7a;
    --paper: #ffffff;
    --backdrop: #e9e9e9;
  }
  * { box-sizing: border-box; margin: 0; padding: 0; }
  html, body { width: 1200px; height: 982px; overflow: hidden; }
  body {
    background: var(--backdrop);
    font-family: "Montserrat", sans-serif;
    position: relative;
  }
  .card {
    position: absolute;
    width: 620px;
    height: 354px;
    background: var(--paper);
    overflow: hidden;
    box-shadow: 0 0 0 3px var(--brand-blue), 0 14px 30px rgba(0,0,0,0.12);
  }
  .card--message { left: 290px; top: 86px; }
  .card--contact { left: 290px; top: 540px; }
  .edge-tab {
    position: absolute;
    left: 0;
    width: 9px;
    height: 34px;
    background: var(--brand-blue);
  }
  .card--message .edge-tab { top: 150px; }
  .card--contact .edge-tab { top: 232px; }

  /* Message side */
  .statement {
    position: absolute;
    color: var(--brand-blue);
    font-weight: 400;
    font-size: 54px;
    line-height: 1;
    letter-spacing: 0.5px;
    white-space: nowrap;
  }
  .prompt {
    position: absolute;
    color: var(--muted);
    font-weight: 400;
    font-size: 15px;
    letter-spacing: 3px;
    white-space: nowrap;
  }
  .rule {
    position: absolute;
    height: 1px;
    background: var(--brand-blue);
  }
  .s-we-help  { left: 40px;  top: 52px; }
  .s-achieve  { left: 322px; top: 96px; }
  .s-by       { left: 424px; top: 144px; }
  .s-because  { left: 346px; top: 192px; }
  .p-target   { left: 56px;  top: 132px; }
  .p-outcome  { left: 72px;  top: 180px; }
  .p-approach { left: 92px;  top: 228px; }
  .p-beliefs  { left: 352px; top: 264px; }
  .r-top      { left: 276px; top: 76px;  width: 314px; }
  .r-mid      { left: 100px; top: 274px; width: 236px; }
  .r-bottom   { left: 100px; top: 318px; width: 200px; }

  /* Contact side */
  .wordmark {
    position: absolute;
    right: 32px;
    top: 62px;
    color: var(--brand-blue);
    font-weight: 800;
    font-size: 44px;
    line-height: 1;
    letter-spacing: 1px;
  }
  .divider {
    position: absolute;
    left: 290px;
    top: 150px;
    width: 298px;
    height: 1px;
    background: var(--rule);
  }
  .person {
    position: absolute;
    left: 60px;
    top: 200px;
  }
  .person__name {
    color: var(--ink);
    font-weight: 800;
    font-size: 26px;
    letter-spacing: 0.5px;
  }
  .person__role {
    color: var(--ink);
    font-weight: 400;
    font-size: 15px;
    letter-spacing: 2px;
    margin-top: 2px;
  }
  .contact {
    position: absolute;
    left: 372px;
    top: 176px;
    list-style: none;
    color: var(--ink);
    font-size: 13px;
    line-height: 1.45;
  }
  .contact li { display: flex; align-items: flex-start; gap: 7px; }
  .contact svg { width: 12px; height: 12px; margin-top: 3px; flex: none; fill: var(--brand-blue); }
</style>
</head>
<body>

<section class="card card--message" aria-label="Brand statement side">
  <span class="edge-tab"></span>
  <div class="statement s-we-help">we help</div>
  <div class="rule r-top"></div>
  <div class="prompt p-target">[ target demographic ]</div>
  <div class="statement s-achieve">achieve</div>
  <div class="prompt p-outcome">[ desired emotional outcome ]</div>
  <div class="statement s-by">by</div>
  <div class="prompt p-approach">[ our unique approch ]</div>
  <div class="statement s-because">because</div>
  <div class="rule r-mid"></div>
  <div class="prompt p-beliefs">[ our brand beliefs ]</div>
  <div class="rule r-bottom"></div>
</section>

<section class="card card--contact" aria-label="Contact side">
  <span class="edge-tab"></span>
  <div class="wordmark">Brightfable</div>
  <div class="divider"></div>
  <div class="person">
    <div class="person__name">Dana Whitfield</div>
    <div class="person__role">Brand Consultant</div>
  </div>
  <ul class="contact">
    <li>
      <svg viewBox="0 0 12 12" aria-hidden="true"><path d="M6 0a4 4 0 0 0-4 4c0 3 4 8 4 8s4-5 4-8a4 4 0 0 0-4-4zm0 5.6A1.6 1.6 0 1 1 6 2.4a1.6 1.6 0 0 1 0 3.2z"/></svg>
      <span>4820 Harbor Lane, Ste 210<br>Westfield, CA 90210</span>
    </li>
    <li>
      <svg viewBox="0 0 12 12" aria-hidden="true"><path d="M2.4 0.5l2 2.2-1 1.4a7 7 0 0 0 4.5 4.5l1.4-1 2.2 2-1.2 1.9C5 11.3 0.7 7 0.5 1.7z"/></svg>
      <span>(555) 014 2290</span>
    </li>
    <li>
      <svg viewBox="0 0 12 12" aria-hidden="true"><path d="M0 2.5h12v7H0zM0.8 3.2L6 6.8l5.2-3.6" stroke="#fff" stroke-width="0.8"/></svg>
      <span>dana@brightfable.com</span>
    </li>
  </ul>
</section>

</body>
</html>
```